Scholarly Pathways - educational consulting

I am beginning an Scholarly Pathways business - focusing on Tribal (Native American Indian) Communities, but will work with anyone. I have work experience in K-12 and Higher Education. Special Education - transition from school to work. Advising and facilitating with academic skills in higher education. I have a BS - Special Education, Masters - Educational Administration and working on a PhD in Higher Education. Also completing PMB approved certification as an Academic Life Coach

Target Market(s)

K12 college bound students and parents, Kinfolk Crossings college bound students and families, special education college bound students and parents

Industry/Entity Type

Business

Contact Information for Business Card

Marnie Odell Fenwick. PO Box 417, Cushing, OK 74023. (918) 555-0293. marnie@scholarlypathways.example

Requirements
Must have
• Scholarly Pathways is the name of the business - Kinfolk Crossings is a focus area
Nice to have
• Tourquoise would be nice. I do not have a logo yet

```html
<!DOCTYPE html>
<html lang="en">
<head>
<meta charset="utf-8">
<title>Scholarly Pathways – Business Card</title>
<link rel="stylesheet" href="https://fonts.googleapis.com/css2?family=Kanit:wght@300;400&display=swap">
<style>
  :root {
    --backdrop: #e9e6e1;
    --card-white: #ffffff;
    --brand-red: #e4141b;
    --brand-red-deep: #c70f15;
    --brand-red-light: #ee2a2f;
    --charcoal: #2b2b2d;
    --ink: #232326;
    --muted: #6d6d72;
  }
  * { margin: 0; padding: 0; box-sizing: border-box; }
  html, body {
    width: 1200px;
    height: 800px;
    overflow: hidden;
    background: var(--backdrop);
    font-family: "Kanit", "Helvetica Neue", Arial, sans-serif;
  }
  .canvas {
    position: relative;
    width: 1200px;
    height: 800px;
  }
  .business-card {
    position: absolute;
    left: 180px;
    top: 160px;
    width: 840px;
    height: 480px;
    background: var(--card-white);
    overflow: hidden;
    box-shadow: 0 8px 24px rgba(0,0,0,0.12);
  }
  .card-shapes {
    position: absolute;
    inset: 0;
    width: 840px;
    height: 480px;
  }
  .shape-red { fill: var(--brand-red); }
  .shape-red-deep { fill: var(--brand-red-deep); }
  .shape-red-light { fill: var(--brand-red-light); }
  .shape-charcoal { fill: var(--charcoal); }

  .brand {
    position: absolute;
    left: 350px;
    top: 74px;
    display: flex;
    align-items: center;
    gap: 14px;
  }
  .brand-dot {
    width: 36px;
    height: 36px;
    border-radius: 50%;
    background: var(--brand-red);
    flex: none;
  }
  .brand-name {
    font-weight: 300;
    font-size: 28px;
    letter-spacing: 1.2px;
    color: var(--ink);
    text-transform: uppercase;
    line-height: 1;
    white-space: nowrap;
  }

  .contact-person {
    position: absolute;
    left: 302px;
    top: 206px;
  }
  .person-row {
    display: flex;
    align-items: center;
    gap: 14px;
  }
  .icon-person { width: 20px; height: 20px; fill: var(--brand-red); flex: none; }
  .person-name {
    font-weight: 400;
    font-size: 29px;
    color: var(--ink);
    letter-spacing: 0.4px;
    line-height: 1.2;
    white-space: nowrap;
  }
  .credentials {
    margin-left: 34px;
    margin-top: 4px;
    font-weight: 300;
    font-size: 18px;
    color: var(--muted);
    line-height: 1.3;
    white-space: nowrap;
  }

  .contact-address {
    position: absolute;
    left: 302px;
    top: 344px;
    display: flex;
    align-items: flex-start;
    gap: 16px;
  }
  .icon-pin { width: 20px; height: 28px; fill: var(--ink); margin-top: 2px; flex: none; }
  .address-text {
    font-weight: 300;
    font-size: 22px;
    color: var(--ink);
    line-height: 1.35;
    letter-spacing: 0.3px;
    white-space: nowrap;
  }
</style>
</head>
<body>
  <main class="canvas">
    <article class="business-card">
      <svg class="card-shapes" viewBox="0 0 840 480" aria-hidden="true">
        <polygon class="shape-red" points="0,0 316,0 170,480 0,480"/>
        <polygon class="shape-red-light" points="0,0 316,0 226,290"/>
        <polygon class="shape-charcoal" points="0,130 170,480 0,480"/>
        <polygon class="shape-red" points="809,0 840,0 840,480 655,480"/>
        <polygon class="shape-red-deep" points="840,170 840,480 720,480"/>
      </svg>

      <div class="brand">
        <span class="brand-dot"></span>
        <span class="brand-name">Scholarly Pathways</span>
      </div>

      <section class="contact-person">
        <div class="person-row">
          <svg class="icon-person" viewBox="0 0 20 20" aria-hidden="true">
            <circle cx="10" cy="5.5" r="4.5"/>
            <path d="M1 20 C1 13 5 11 10 11 C15 11 19 13 19 20 Z"/>
          </svg>
          <h1 class="person-name">Marnie Odell Fenwick</h1>
        </div>
        <p class="credentials">BS - Special Education<br>Masters - Educational Administration</p>
      </section>

      <section class="contact-address">
        <svg class="icon-pin" viewBox="0 0 20 28" aria-hidden="true">
          <path d="M10 0 C4.5 0 0 4.3 0 9.7 C0 17 10 28 10 28 C10 28 20 17 20 9.7 C20 4.3 15.5 0 10 0 Z M10 13.5 A4 4 0 1 1 10 5.5 A4 4 0 1 1 10 13.5 Z"/>
        </svg>
        <p class="address-text">P.O. Box 417 Alderbrook,<br>ZZ 00417 555.555.0293</p>
      </section>
    </article>
  </main>
</body>
</html>
```